Reed & Vale NC grand opening (for BILLBOARD)

Advertising the grand opening of our cannabis/hemp shop in NC. We will sell all things hemp (flower, cartridges, disposables, edibles, creams, lotions, pet products etc...)

Requirements
Must have
• include, open starting Aug 1, but grand opening Aug 15th.
Nice to have
• Difference slogan ideas "Save some cash, buy our grass" "Find your perfect high at Reed & Vale cannabis store" "Experience Nature's Gift: Reed & Vale Cannabis Store"

```html
<!DOCTYPE html>
<html lang="en">
<head>
<meta charset="utf-8">
<title>Reed &amp; Vale — Grand Opening Billboard</title>
<link href="https://fonts.googleapis.com/css2?family=Poppins:wght@500;600;800&display=swap" rel="stylesheet">
<style>
  :root {
    --page-bg: #d4d4d4;
    --forest-deep: #142a0b;
    --forest: #1f3a14;
    --forest-soft: #2f4f22;
    --leaf-green: #7cc242;
    --white: #ffffff;
    --photo-warm: #8a6a4a;
    --photo-sage: #6f8a62;
  }
  * { box-sizing: border-box; margin: 0; padding: 0; }
  html, body {
    width: 1200px; height: 456px; overflow: hidden;
    background: var(--page-bg);
    font-family: "Poppins", Arial, sans-serif;
  }
  .billboard {
    position: absolute; left: 73px; top: 63px;
    width: 1054px; height: 308px; overflow: hidden;
    background:
      radial-gradient(ellipse at 55% 0%, var(--forest-soft) 0%, transparent 60%),
      linear-gradient(90deg, var(--forest) 0%, var(--forest-deep) 100%);
    box-shadow: 4px 6px 10px rgba(0,0,0,0.25);
  }
  .product-photo {
    position: absolute; left: 0; top: 0; width: 370px; height: 308px;
    background:
      radial-gradient(ellipse at 45% 72%, var(--photo-warm) 0%, transparent 40%),
      radial-gradient(ellipse at 20% 35%, var(--photo-sage) 0%, transparent 55%),
      linear-gradient(90deg, #5e6e55 0%, #3a4c30 65%, rgba(31,58,20,0) 100%);
  }
  .foliage-corner {
    position: absolute; right: 0; bottom: 0; width: 236px; height: 182px;
    background: radial-gradient(ellipse at 80% 85%, #4f8a2a 0%, #2e5a1a 45%, rgba(20,42,11,0) 75%);
  }
  .brand-name {
    position: absolute; right: 28px; top: 24px;
    font-weight: 600; font-size: 38px; line-height: 56px;
    color: var(--leaf-green); white-space: nowrap;
  }
  .headline {
    position: absolute; left: 373px; top: 52px;
    font-weight: 800; font-size: 54px; line-height: 58px;
    color: var(--white); letter-spacing: 0.5px; text-transform: uppercase;
    white-space: nowrap;
  }
  .headline .accent { color: var(--leaf-green); }
  .store-line {
    position: absolute; left: 373px; top: 176px; width: 452px;
    border-top: 1px solid rgba(124,194,66,0.7);
    border-bottom: 1px solid rgba(124,194,66,0.7);
    padding: 3px 0 4px;
    font-weight: 600; font-size: 28px; line-height: 34px;
    color: var(--white); text-transform: uppercase; white-space: nowrap;
  }
  .opening-dates {
    position: absolute; left: 373px; top: 226px;
    font-weight: 600; font-size: 17px; line-height: 24px;
    color: var(--leaf-green); text-transform: uppercase; white-space: nowrap;
  }
  .location {
    position: absolute; left: 373px; top: 257px;
    display: flex; align-items: center; gap: 10px;
    font-weight: 500; font-size: 20px; line-height: 26px;
    color: var(--white); text-transform: uppercase; white-space: nowrap;
  }
  .location svg { width: 20px; height: 22px; }
</style>
</head>
<body>
  <div class="billboard">
    <div class="product-photo" role="img" aria-label="Hemp oil dropper bottle, jar and seeds in a wooden bowl with cannabis leaves on a table"></div>
    <div class="foliage-corner" role="img" aria-label="Cannabis leaves in the lower right corner"></div>

    <div class="brand-name">Reed &amp; Vale</div>

    <h1 class="headline">Find your<br><span class="accent">Perfect high</span> at</h1>
    <p class="store-line">Reed &amp; Vale cannabis store</p>
    <p class="opening-dates">Open Aug 1 &middot; Grand Opening Aug 15</p>
    <p class="location">
      <svg viewBox="0 0 20 22" aria-hidden="true">
        <path d="M10 0C4.8 0 1 3.9 1 8.8 1 15 10 22 10 22s9-7 9-13.2C19 3.9 15.2 0 10 0z" fill="var(--leaf-green)"/>
        <circle cx="10" cy="8.6" r="3.4" fill="var(--forest)"/>
      </svg>
      Off exit 6A Birchmont Rd
    </p>
  </div>
</body>
</html>
```